Web Site

Target Market(s)

CEOs and International Sales & Marketing Directors of International Companies who wish to expand their business reach to Dubai and the Middle East and are looking for a local professional partner to work with.

Requirements
Must have
• Creativity is key. We don't want the normal standard boxes of text and boxes of pics. Be as creative as you like.
Nice to have
• (This is only a suggestion, we welcome your creativity)
- The center of all pages could be large rotating pictures which display professional corporate men/women working in an office, images of Dubai, the UAE, skyscrapers of business towers in Dubai, ..etc.
- Images should reflect Dubai and the Arab World as a modern, fast-paced, growing modern market - Not Traditional)
Should not have
• Not so colorful, the fewer colors you use, the better.
Not Crammed or Busy
Not Traditional but modern

```html
<!DOCTYPE html>
<html lang="en">
<head>
<meta charset="utf-8">
<title>Kernel Group – Contact</title>
<link href="https://fonts.googleapis.com/css2?family=Questrial&family=PT+Sans:wght@400;700&display=swap" rel="stylesheet">
<style>
  :root {
    --brand-red: #8c1c1c;
    --brand-red-light: #a93030;
    --brand-red-dark: #761212;
    --ink: #111111;
    --text-grey: #666666;
    --muted: #7a7a7a;
    --line: #d8d8d8;
    --paper: #ffffff;
    --dot-grey: #555555;
    --hero-tint-a: #f7f5f5;
    --hero-tint-b: #ebe6e6;
    --pattern-tint: #f6eded;
  }
  * { box-sizing: border-box; margin: 0; padding: 0; }
  html, body { width: 1200px; height: 1181px; overflow: hidden; }
  body { position: relative; background: var(--paper); font-family: 'PT Sans', sans-serif; color: var(--ink); }
  .abs { position: absolute; }

  .top-rule { left: 0; top: 0; width: 1200px; height: 3px; background: #111; }
  .header-band { left: 0; top: 3px; width: 1200px; height: 631px;
    background: linear-gradient(#f3f3f3 0, #ffffff 45px, #ffffff 150px, #efefef 260px, #ebebeb 600px, #f2f2f2 631px); }

  .utility-links { right: 90px; top: 13px; font-size: 13px; color: var(--brand-red); }
  .utility-links span.sep { margin: 0 9px; }

  .brand { left: 50px; top: 70px; font-family: 'Questrial', sans-serif; color: var(--ink); }
  .brand-name { font-size: 46px; line-height: 1; letter-spacing: 1px; }
  .brand-sub { font-size: 17px; letter-spacing: 16px; margin-top: 6px; padding-left: 4px; }

  .search { left: 861px; top: 97px; width: 270px; height: 33px; background: #fff;
    border: 1px solid #e2e2e2; box-shadow: 0 3px 6px rgba(0,0,0,.12);
    font-size: 12px; font-style: italic; color: var(--brand-red); padding: 9px 10px; }
  .search-go { left: 1126px; top: 96px; width: 38px; height: 38px; border-radius: 50%;
    background: var(--brand-red); color: #fff; font-size: 13px; text-align: center; line-height: 38px; }

  .main-nav { left: 27px; top: 173px; width: 1143px; height: 53px; display: flex;
    background: linear-gradient(var(--brand-red-light), var(--brand-red-dark));
    border-radius: 3px 3px 0 0; }
  .main-nav a { color: #fff; text-decoration: none; font-size: 16px; display: flex;
    align-items: center; justify-content: center; border-right: 1px solid rgba(255,255,255,.35); }
  .main-nav a:last-child { border-right: none; }

  .slider { left: 27px; top: 226px; width: 1145px; height: 382px; background: #fff;
    box-shadow: 0 4px 10px rgba(0,0,0,.12); overflow: hidden; }
  .hero-visual { left: 540px; top: 0; width: 605px; height: 382px;
    background: linear-gradient(100deg, #ffffff 0%, var(--hero-tint-a) 30%, var(--hero-tint-b) 100%); }
  .hero-pattern { left: 49px; top: 284px; width: 416px; height: 98px;
    background: linear-gradient(180deg, rgba(246,237,237,0) 0%, var(--pattern-tint) 60%, rgba(246,237,237,.6) 100%); }

  .slide-title { left: 107px; top: 288px; font-family: 'Questrial', sans-serif; font-size: 29px; color: var(--ink); }
  .slide-title em { font-style: normal; color: var(--brand-red); }
  .slide-sub { left: 107px; top: 328px; font-family: 'Questrial', sans-serif; font-size: 20px; color: var(--brand-red); }
  .slide-rule { left: 107px; top: 366px; width: 356px; height: 1px; background: linear-gradient(90deg, #e8d4d4, #f6eeee); }
  .slide-text { left: 107px; top: 380px; width: 370px; font-size: 13px; line-height: 21px; color: var(--text-grey); }
  .btn-dark { background: linear-gradient(#2a2a2a, #000); color: #fff; border-radius: 4px;
    font-size: 14px; display: flex; align-items: center; justify-content: center; gap: 6px; }
  .learn-more { left: 108px; top: 457px; width: 105px; height: 30px; }
  .slide-dots { left: 215px; top: 535px; display: flex; gap: 19px; }
  .slide-dots i { width: 13px; height: 13px; border-radius: 50%; background: var(--dot-grey); display: block; }
  .slide-dots i.active { background: var(--brand-red); }

  .section-title { left: 39px; top: 673px; font-family: 'Questrial', sans-serif; font-size: 20px; font-weight: 400; color: var(--ink); }
  .section-title em { font-style: normal; color: var(--brand-red); }

  .column-intro { font-family: 'Questrial', sans-serif; font-size: 17px; color: var(--muted); top: 744px; }
  .contact-methods { left: 46px; top: 792px; font-family: 'Questrial', sans-serif; font-size: 17px; }
  .method { position: absolute; left: 0; white-space: nowrap; }
  .method .label { position: absolute; left: 0; color: var(--ink); }
  .method .colon { position: absolute; left: 95px; }
  .method .value { position: absolute; left: 110px; color: var(--brand-red); line-height: 23px; }

  .contact-form { font-family: 'Questrial', sans-serif; font-size: 17px; }
  .form-label { right: 510px; color: var(--ink); white-space: nowrap; }
  .field { left: 704px; width: 210px; height: 28px; border: 1px solid #bcbcbc; border-radius: 2px;
    background: linear-gradient(#eeeeee, #ffffff 40%); }
  .field.textarea { height: 87px; }
  .submit { left: 932px; top: 982px; width: 104px; height: 31px; }

  .footer { left: 0; top: 1078px; width: 1200px; height: 103px; border-top: 1px solid var(--line);
    background: linear-gradient(#fafafa, #f0f0f0); }
  .footer-links { left: 0; top: 1104px; width: 1200px; text-align: center; font-size: 13px; color: var(--muted); }
  .footer-links .sep { margin: 0 11px; }
  .copyright { left: 0; top: 1139px; width: 1200px; text-align: center; font-size: 12px; color: var(--muted); }
</style>
</head>
<body>
  <div class="abs top-rule"></div>
  <div class="abs header-band"></div>

  <div class="abs utility-links">FAQ's<span class="sep">|</span>Support<span class="sep">|</span>Contact info</div>

  <div class="abs brand">
    <div class="brand-name">KERNEL</div>
    <div class="brand-sub">GROUP</div>
  </div>

  <div class="abs search">SEARCH HERE..</div>
  <div class="abs search-go">GO</div>

  <nav class="abs main-nav">
    <a style="width:105px">Home</a>
    <a style="width:173px">About the Group</a>
    <a style="width:191px">Chairman’s Message</a>
    <a style="width:118px">Divisions</a>
    <a style="width:178px">Group Companies</a>
    <a style="width:241px">Employment &amp; Association</a>
    <a style="width:137px">Contact us</a>
  </nav>

  <div class="abs slider">
    <div class="abs hero-visual" role="img" aria-label="Rotating hero photograph: modern Dubai business towers and professionals at work"></div>
    <div class="abs hero-pattern" role="img" aria-label="Faint decorative brand pattern"></div>
  </div>
  <div class="abs slide-title">KERNEL GROUP <em>PUCH LINE..</em></div>
  <div class="abs slide-sub">tittle line goes here</div>
  <div class="abs slide-rule"></div>
  <p class="abs slide-text">It’s the simplest, cheapest and also the basic thing the search engine picks it up very easily. We at Brightline Studio provide you the best simple websites too.</p>
  <div class="abs btn-dark learn-more">learn more
    <svg width="8" height="10" viewBox="0 0 8 10"><path d="M2 1l4 4-4 4" stroke="#fff" stroke-width="2" fill="none"/></svg>
  </div>
  <div class="abs slide-dots"><i class="active"></i><i></i><i></i><i></i><i></i></div>

  <h1 class="abs section-title"><em>Contact</em> Kernel Group</h1>

  <p class="abs column-intro" style="left:42px">You may reach us by the following methods:</p>
  <div class="abs contact-methods">
    <div class="method" style="top:0"><span class="label">Address</span><span class="colon">:</span><span class="value">#24 Duis aute irure<br>&nbsp;reprehen derit</span></div>
    <div class="method" style="top:63px"><span class="label">Telephone</span><span class="colon" style="left:108px">:</span><span class="value" style="left:108px">&nbsp;&nbsp;+971 4 555 0148</span></div>
    <div class="method" style="top:103px"><span class="label">Fax</span><span class="colon">:</span><span class="value">+971 4 555 0149</span></div>
    <div class="method" style="top:143px"><span class="label">E mail</span><span class="colon">:</span><span class="value">info@kernelgroup.com</span></div>
  </div>

  <p class="abs column-intro" style="left:524px">Please fill in the contact form with the following details</p>
  <div class="contact-form">
    <div class="abs form-label" style="top:792px">Name &nbsp;:</div>
    <div class="abs field" style="top:790px"></div>
    <div class="abs form-label" style="top:839px">Mobile &nbsp;:</div>
    <div class="abs field" style="top:837px"></div>
    <div class="abs form-label" style="top:886px">E mail &nbsp;:</div>
    <div class="abs field" style="top:884px"></div>
    <div class="abs form-label" style="top:932px">Enquiry/Questions &nbsp;:</div>
    <div class="abs field textarea" style="top:927px"></div>
    <div class="abs btn-dark submit">SUBMIT
      <svg width="8" height="10" viewBox="0 0 8 10"><path d="M2 1l4 4-4 4" stroke="#fff" stroke-width="2" fill="none"/></svg>
    </div>
  </div>

  <footer class="abs footer"></footer>
  <div class="abs footer-links">Home<span class="sep">|</span>About the Group<span class="sep">|</span>Chairman’s Message<span class="sep">|</span>Divisions<span class="sep">|</span>Group Companies<span class="sep">|</span>Employment &amp; Association<span class="sep">|</span>Contact us</div>
  <div class="abs copyright">© 2012 Company Name &nbsp;|&nbsp; All right reserved</div>
</body>
</html>
```